VORL Pty Ltd Business Card

Looking for a simple yet eye-catching double-sided business card design using my company logo on one side and contact details on the other.

Target Market(s)

Government

Industry/Entity Type

Communication Systems Engineering

Contact Information for Business Card

VORL Pty Ltd

Requirements
Nice to have
• Would be great to have a QR code so details can be scanned into contacts

```html
<!DOCTYPE html>
<html lang="en">
<head>
<meta charset="utf-8">
<title>VORL Pty Ltd Business Card</title>
<link href="https://fonts.googleapis.com/css2?family=Open+Sans:wght@400;600;700&display=swap" rel="stylesheet">
<style>
  :root {
    --backdrop: #2f2f2f;
    --slate: #37424a;
    --slate-deep: #2b343b;
    --paper: #ffffff;
    --ink: #1f2326;
    --mist: #c9c9c9;
  }
  * { margin: 0; padding: 0; box-sizing: border-box; }
  html, body {
    width: 1200px; height: 780px; overflow: hidden;
    background: var(--backdrop);
    font-family: "Open Sans", Arial, sans-serif;
  }
  .sheet {
    width: 1200px; height: 780px;
    display: flex; align-items: center; justify-content: center; gap: 40px;
  }
  .card {
    width: 540px; height: 310px; position: relative; overflow: hidden;
  }
  .card--front {
    background: var(--slate);
    display: flex; align-items: center; justify-content: center;
  }
  .front-wordmark {
    font-weight: 700; font-size: 92px; letter-spacing: 6px;
    color: var(--slate-deep);
  }
  .card--back { background: var(--paper); }
  .back-brand {
    position: absolute; left: 34px; top: 70px;
    display: flex; align-items: center; gap: 18px;
  }
  .brand-dot {
    width: 64px; height: 64px; border-radius: 50%;
    background: var(--slate);
  }
  .brand-name {
    font-weight: 700; font-size: 52px; letter-spacing: 4px; color: var(--slate);
  }
  .holder {
    position: absolute; right: 30px; top: 22px; text-align: right;
  }
  .holder-name { font-weight: 700; font-size: 26px; color: var(--slate); line-height: 1.1; }
  .holder-role { font-weight: 600; font-size: 13px; color: var(--ink); }
  .edge-bar {
    position: absolute; right: 0; top: 22px; width: 16px; height: 46px;
    background: var(--slate);
  }
  .decor {
    position: absolute; right: 0; top: 92px; width: 230px; height: 200px;
    background: radial-gradient(ellipse at 55% 45%, #e6e6e6 0%, #f2f2f2 55%, var(--paper) 80%);
  }
  .contact {
    position: absolute; left: 34px; bottom: 22px;
    font-size: 14px; color: var(--ink); line-height: 1.35;
  }
  .address { margin-bottom: 8px; }
  .contact-line { display: flex; align-items: center; gap: 8px; }
  .contact-line svg { width: 13px; height: 13px; flex: none; }
</style>
</head>
<body>
<main class="sheet">
  <section class="card card--front">
    <span class="front-wordmark">VORL</span>
  </section>

  <section class="card card--back">
    <div class="back-brand">
      <span class="brand-dot"></span>
      <span class="brand-name">VORL</span>
    </div>

    <div class="holder">
      <p class="holder-name">Dana Whitlock</p>
      <p class="holder-role">Co-Founder</p>
    </div>
    <span class="edge-bar"></span>

    <div class="decor" role="img" aria-label="Faint circuit-tree decoration"></div>

    <div class="contact">
      <p class="address">14-16 Harlow Lane Redfern Bay<br>NSW 2099 Australia</p>
      <p class="contact-line">
        <svg viewBox="0 0 16 16"><path d="M4 1l3 3-2 2c1 2 3 4 5 5l2-2 3 3-2 3C7 15 1 9 1 3z" fill="#333"/></svg>
        (817) 555-0142
      </p>
      <p class="contact-line">
        <svg viewBox="0 0 16 16"><circle cx="8" cy="8" r="7" fill="#333"/><path d="M1 8h14M8 1c3 3 3 11 0 14M8 1c-3 3-3 11 0 14" stroke="#fff" stroke-width="1" fill="none"/></svg>
        www.vorl.com.au
      </p>
      <p class="contact-line">
        <svg viewBox="0 0 16 16"><rect x="1" y="3" width="14" height="10" fill="#333"/><path d="M1 3l7 6 7-6" stroke="#fff" stroke-width="1.2" fill="none"/></svg>
        admin@vorl.com.au
      </p>
    </div>
  </section>
</main>
</body>
</html>
```